Portrait of a Graduate

Our school community has created a document which describes the characteristics that every student who graduates from our school should possess. We would like a visual graphic to present the information to parents\ community. We came up with three buckets (Personal, Social, and Academic) and the concept "BLH Graduates Will Be Okay" is the central theme.
We are open to 2 different concepts:
1. A ven diagram of sorts, where the three buckets are each in an area - and the over lap is "BLH Graduates Will Be Okay"
2. Our logo has a sassafras leaf in it - using the leaves to represent each bucket and the central concept as the stem - or some other creative version.

The text to be used is below:

BLH Graduates Will Be Okay (at the center/on the stem)

1. Personal
They will:
have self-worth
advocate for themselves
feel secure in their future

2. Social
They will:
embrace differences
engage in trusting relationships
be compassionate (members of their community)

3. Academic
They will:
apply skills and strategies
creatively problem-solve
achieve individual success

```html
<!DOCTYPE html>
<html lang="en">
<head>
<meta charset="utf-8">
<title>BLH Graduates – Portrait of a Graduate</title>
<link href="https://fonts.googleapis.com/css2?family=Jost:wght@400&family=Cormorant+Garamond:wght@500&family=Crimson+Text:wght@400&display=swap" rel="stylesheet">
<style>
  :root {
    --gold: #e5b823;
    --navy: #02344a;
    --white: #ffffff;
    --bg-top: #e0e0e0;
    --bg-mid: #f4f4f4;
    --bg-low: #efefef;
  }
  html, body { margin: 0; padding: 0; overflow: hidden; }
  .canvas {
    position: relative;
    width: 1200px;
    height: 1200px;
    overflow: hidden;
    background: linear-gradient(180deg, var(--bg-top) 0%, var(--bg-mid) 75%, var(--bg-low) 100%);
    font-family: "Crimson Text", Georgia, serif;
  }
  .headline {
    position: absolute;
    left: 62px;
    top: 86px;
    margin: 0;
    font-family: "Jost", "Helvetica Neue", sans-serif;
    font-weight: 400;
    font-size: 76px;
    letter-spacing: 3px;
    line-height: 1;
    color: var(--gold);
  }
  .school-name {
    position: absolute;
    left: 852px;
    top: 60px;
    width: 300px;
    display: flex;
    align-items: center;
    gap: 12px;
    color: var(--navy);
    font-family: "Crimson Text", Georgia, serif;
    font-size: 27px;
    line-height: 1.1;
  }
  .school-name .mark {
    flex: 0 0 auto;
    width: 22px;
    height: 22px;
    border-radius: 50%;
    background: var(--navy);
  }
  .shapes { position: absolute; left: 0; top: 0; }
  .pillar { position: absolute; color: var(--white); }
  .pillar .number {
    position: absolute;
    font-family: "Cormorant Garamond", Georgia, serif;
    font-weight: 500;
    font-size: 70px;
    line-height: 1;
    font-variant-numeric: lining-nums;
    font-feature-settings: "lnum" 1;
    color: var(--gold);
  }
  .pillar .title {
    position: absolute;
    margin: 0;
    font-family: "Cormorant Garamond", Georgia, serif;
    font-weight: 500;
    font-size: 42px;
    line-height: 1;
    color: var(--gold);
    padding-bottom: 6px;
    border-bottom: 2px solid var(--gold);
    white-space: nowrap;
  }
  .pillar ul { position: absolute; margin: 0; padding: 0; list-style: none; white-space: nowrap; }
  .pillar--personal .number { left: 417px; top: 330px; }
  .pillar--personal .title { left: 391px; top: 412px; }
  .pillar--personal ul { left: 424px; top: 464px; font-size: 18px; line-height: 20px; }
  .pillar--personal li:nth-child(2) { padding-left: 4px; }
  .pillar--personal li:nth-child(3) { padding-left: 9px; }
  .pillar--personal li:nth-child(4) { padding-left: 14px; }
  .pillar--academic .number { left: 119px; top: 644px; }
  .pillar--academic .title { left: 232px; top: 674px; }
  .pillar--academic ul { left: 312px; top: 724px; font-size: 18px; line-height: 25px; }
  .pillar--social .title { left: 892px; top: 660px; }
  .pillar--social .number { left: 1063px; top: 656px; }
  .pillar--social ul { left: 827px; top: 710px; font-size: 16.5px; line-height: 17.5px; }
  .pillar--social li.continued { padding-left: 71px; }
  .theme {
    position: absolute;
    left: 352px;
    top: 912px;
    margin: 0;
    font-family: "Jost", "Helvetica Neue", sans-serif;
    font-weight: 400;
    color: var(--gold);
    line-height: 1;
  }
  .theme .line1 { display: block; font-size: 44px; letter-spacing: 1.5px; }
  .theme .line2 { display: block; font-size: 54px; letter-spacing: 1px; margin-top: 6px; }
</style>
</head>
<body>
<main class="canvas">
  <h1 class="headline">BLH GRADUATES</h1>

  <div class="school-name">
    <span class="mark"></span>
    <span>The Bramble Lane School at Hollis</span>
  </div>

  <svg class="shapes" width="1200" height="1200" viewBox="0 0 1200 1200" role="img" aria-label="Three navy panels for the Personal, Academic and Social qualities joined by a stem">
    <g stroke="var(--navy)" stroke-width="16" stroke-linecap="round" fill="none">
      <path d="M600 560 L680 760"/>
      <path d="M560 745 L680 760 L785 750"/>
      <path d="M680 760 C722 820 748 900 742 985"/>
    </g>
    <rect x="370" y="280" width="268" height="290" rx="60" fill="var(--navy)"/>
    <rect x="75" y="605" width="490" height="265" rx="60" fill="var(--navy)"/>
    <rect x="780" y="630" width="382" height="240" rx="60" fill="var(--navy)"/>
  </svg>

  <section class="pillar pillar--personal">
    <span class="number">02</span>
    <h2 class="title">PERSONAL</h2>
    <ul>
      <li>They will:</li>
      <li>have self-worth</li>
      <li>advocate for themselves</li>
      <li>feel secure in their future</li>
    </ul>
  </section>

  <section class="pillar pillar--academic">
    <span class="number">01</span>
    <h2 class="title">ACADEMIC</h2>
    <ul>
      <li>They will:</li>
      <li>apply skills and strategies</li>
      <li>creatively problem-solve</li>
      <li>achieve individual success</li>
    </ul>
  </section>

  <section class="pillar pillar--social">
    <h2 class="title">SOCIAL</h2>
    <span class="number">03</span>
    <ul>
      <li>They will:</li>
      <li>embrace differences</li>
      <li>engage in trusting</li>
      <li>relationships</li>
      <li>be compassionate (members</li>
      <li class="continued">of their community)</li>
    </ul>
  </section>

  <p class="theme">
    <span class="line1">BLH GRADUATES</span>
    <span class="line2">WILL BE OKAY</span>
  </p>
</main>
</body>
</html>
```